Lantern Hours (A Romance novel set in Britain by a castle in Northumberland. Gothic themes, mostly c

I need the first of four book covers in a series of traditional old-fashioned love stories with a strong heroine, a strong masculine hero, and some history. Each is set in a different place in Britain, in the modern day with a backdrop of heritage. While some of Marla Venning's books are contemporary with a sexy side, or an American modern twist, these are very much for an older market, longer books with a real story with many subplots. These are heartache books, delayed romance, difficulties in communication but high passion. They are set by the English coast, all home from home for the lead hero and heroine, both of whom are attracted to the sea and the beach. A castle, ruined, features in each. These are books a 20 year old who loved Rosa Thimm will read, as well as your grandma who has read romance all her life. They are substantial books with a heart and some research. The covers need to appeal to all and capture the history of romance as a genre.
Marla Venning's books on The Salt Winds are featured on her site www.marlavenning-example.com in Fiction and have the dark gothic colours of her modern romance. These upcoming books should complement these but be for an older crowd with less suggestion of sex. Place is important, history is more important. Castles and tortured hearts are important. Soulful, deep thinking and self discovery.
This book Lantern Hours is set at Craster Bay and should feature the bay and castle: we want to see some sea. Fellwick Castle is the ruined castle. There are plenty of images to draw from. If this is too difficult, a couple walking on an English coastline beach would possibly work in the right colours. There must be sea, and no island style! Gothic themes are there, so a little bit darker on the colour wheel is good, but this is still a hopeful romance.
While they are outdated, one idea I like is the revival Nora Vellacott style cover I attach with the small image. I also attach other covers with the same idea or mood. I prefer photgraphic here if we go with a couple on the beach. She is in her mid 20s, him is mid to late 30s. She is dark haired. He is American. They would be in today's dress, smart casual.
Title: Lantern Hours
Author: Marla Venning
I need e and print please. The press logo, Perlowe, is attached for the spine. Back copy to follow.

```html
<!DOCTYPE html>
<html lang="en">
<head>
<meta charset="utf-8">
<title>Lantern Hours – Cover Wrap</title>
<link rel="stylesheet" href="https://fonts.googleapis.com/css2?family=Oswald:wght@300;400&family=Roboto+Condensed:wght@300;400&display=swap">
<style>
  :root {
    --page-bg: #ffffff;
    --ink-light: #ffffff;
    --ink-soft: rgba(255,255,255,0.86);
    --spine-author: #a9d8f5;
    --sky-pale: #dfe9f0;
    --sky-blue: #a9c6dc;
    --hill-mist: #7f98ad;
    --sea-bright: #3f86b8;
    --sea-mid: #2f6f9f;
    --rock-mauve: #6d6a78;
    --rock-dark: #3a4557;
    --shore-deep: #1b2a3d;
    --back-top: #3b82b6;
    --back-mid: #2c6fa2;
    --back-low: #3a77a3;
    --back-deep: #5a7f9a;
    --spine-top: #3f86bb;
    --spine-deep: #23608f;
  }
  * { box-sizing: border-box; margin: 0; padding: 0; }
  html, body {
    width: 1198px; height: 1200px; overflow: hidden;
    background: var(--page-bg);
  }
  .cover-wrap {
    position: absolute; left: 49px; top: 210px;
    width: 1100px; height: 780px;
    display: flex;
  }
  .back-cover, .front-cover, .spine { position: relative; height: 100%; overflow: hidden; }
  .back-cover { width: 512px; }
  .spine { width: 80px; }
  .front-cover { width: 508px; }

  .back-photo {
    position: absolute; inset: 0;
    background: linear-gradient(180deg, var(--back-top) 0%, var(--back-mid) 40%, var(--back-low) 75%, var(--back-deep) 100%);
  }
  .back-title {
    position: relative; text-align: center;
    padding-top: 96px;
    font-family: "Oswald", sans-serif; font-weight: 300;
    font-size: 27px; letter-spacing: 0.5px; color: var(--ink-light);
  }
  .back-copy {
    position: relative;
    margin: 38px 46px 0;
    font-family: "Roboto Condensed", sans-serif; font-weight: 300;
    font-size: 12.5px; line-height: 17.5px; color: var(--ink-soft);
    text-align: center;
  }
  .back-copy p + p { margin-top: 26px; }

  .spine-bg {
    position: absolute; inset: 0;
    background: linear-gradient(180deg, var(--spine-top) 0%, var(--spine-deep) 100%);
  }
  .spine-imprint {
    position: absolute; top: 26px; left: 0; right: 0;
    display: flex; flex-direction: column; align-items: center; gap: 6px;
    font-family: "Oswald", sans-serif; font-weight: 300;
    font-size: 12px; letter-spacing: 1px; color: var(--ink-light);
  }
  .imprint-dot { width: 14px; height: 14px; border-radius: 50%; background: var(--ink-light); }
  .spine-text {
    position: absolute; top: 150px; left: 50%;
    transform: translateX(-50%);
    writing-mode: vertical-rl;
    display: flex; align-items: center; gap: 20px;
    font-family: "Oswald", sans-serif; font-weight: 300;
    white-space: nowrap;
  }
  .spine-title { font-size: 52px; color: var(--ink-light); }
  .spine-author { font-size: 36px; color: var(--spine-author); }

  .front-photo {
    position: absolute; inset: 0;
    background: linear-gradient(180deg,
      var(--sky-pale) 0%,
      var(--sky-blue) 14%,
      var(--hill-mist) 30%,
      var(--sea-bright) 42%,
      var(--sea-mid) 50%,
      var(--rock-mauve) 58%,
      var(--rock-dark) 74%,
      var(--shore-deep) 100%);
  }
  .front-imprint {
    position: absolute; top: 28px; left: 0; right: 0;
    display: flex; flex-direction: column; align-items: center; gap: 6px;
    font-family: "Oswald", sans-serif; font-weight: 400;
    font-size: 19px; letter-spacing: 2px; color: var(--ink-light);
  }
  .front-imprint .imprint-dot { width: 16px; height: 16px; }
  .front-title {
    position: absolute; top: 126px; left: 0; right: 0;
    text-align: center;
    font-family: "Oswald", sans-serif; font-weight: 300;
    font-size: 118px; line-height: 120px; color: var(--ink-light);
    text-transform: uppercase;
  }
  .front-author {
    position: absolute; top: 690px; left: 0; right: 0;
    text-align: center;
    font-family: "Oswald", sans-serif; font-weight: 300;
    font-size: 34px; color: var(--ink-light);
  }
</style>
</head>
<body>
  <main class="cover-wrap">
    <section class="back-cover">
      <div class="back-photo" role="img" aria-label="Soft-focus photograph of a blue sea shore with a couple walking in the distance"></div>
      <h2 class="back-title">LANTERN HOURS</h2>
      <div class="back-copy">
        <p>Marla Venning returns to the northern coast with a story of two strangers who find their way back to the sea and to each other. When Elin comes home to the quiet bay after ten long years away, she expects grey mornings, cold tides and the slow work of mending her late grandmother's cottage. What she finds instead is a ruined castle on the headland, a locked chapter of her family's past, and a visitor from across the ocean who will not leave her thoughts. He is patient, guarded and far too kind, and with every evening walk along the shore the careful walls she built begin, one stone at a time, to fall.</p>
        <p>He came to study the history of the walls, not to fall for the woman who keeps the keys. Yet the long light of summer evenings, the winter storms that close the village road, and the bundle of letters found beneath the chapel floor draw them closer than either would ever choose. Each letter tells of another pair of lovers, parted by war and by pride, whose promise was never kept. As Elin and her visitor trace the story from the archive to the cliffs, old silences echo their own, and the words they most need to say remain unspoken. Between them lies a distance of years, an ocean and a grief neither knows how to name.</p>
        <p>Lantern Hours is a sweeping tale of heartache, patience and hope, set between grey water and broken towers on one of the loveliest stretches of the English coast. It is a story of homecoming and of leaving, of a woman learning to trust her own strength and a man learning that some places hold on to us long after we have gone. Rich in history and full of the wind and light of the northern shore, it moves from quiet village kitchens to the windswept ramparts of the old fortress, from candlelit archives to the wide sands at low tide. Here the past is never quite finished, every ruin keeps a secret, and love must learn to wait for the turning of the tide. For readers who treasure a long, slow, soulful romance with real depth, and for anyone who has ever stood on a beach at dusk and wondered what might have been, this is a book to keep close and return to again and again.</p>
      </div>
    </section>

    <section class="spine">
      <div class="spine-bg"></div>
      <div class="spine-imprint"><span class="imprint-dot"></span><span>PERLOWE</span></div>
      <div class="spine-text">
        <span class="spine-title">LANTERN HOURS</span>
        <span class="spine-author">Marla Venning</span>
      </div>
    </section>

    <section class="front-cover">
      <div class="front-photo" role="img" aria-label="Photograph of a misty coastal bay: pale sky and hills above a bright blue sea, with a couple seen from behind walking hand in hand over dark shore rocks in the foreground"></div>
      <div class="front-imprint"><span class="imprint-dot"></span><span>PERLOWE</span></div>
      <h1 class="front-title">Lantern<br>Hours</h1>
      <p class="front-author">Marla Venning</p>
    </section>
  </main>
</body>
</html>
```